Conference website: Kelvar Civic Forum Meetup 2015

We need a web design to help develop a modern and interactive website for the 2nd Kelvar Civic Meetup which main objective will be to present and discuss real-life Kelvar business initiatives being implemented by entrepreneurs and corporate innovators that are driving sustainable innovation from the bottom up

This is a bi-annual event and will build on the 1st Kelvar Civic Forum Meetup
http://www.kelvarcivicforum.example/summit-2013. It is important that the new website maintain consistency with the 1) the Kelvar Civic Forum Logo (www.kelvarcivicforum.example), 2) the visual identity from the fist event and 3) the organization TQR Logo (www.t7qr.example) -- but the design should be modern, clean, and crisp.

Target Market(s)

Corporations, academics, executives, entrepreneurs, consultants, multilateral organizations, founders, institutions

Industry/Entity Type

Business

Coding

Coded - Design and coding required

Number of Pages Required

5+ page

Font styles to use
Sans Serif

Colors
f68d4d
9bcb3b
3276b5
faa54b
00a88f
0792cd
f37022
9bcb3c
0355a3

Requirements
Must have
• maintain consistency with Kelvar Civic Forum Logo
• dynamic to get the attention
• design modern, clean and crisp
• content should be well linked (e.i. photos and bios liked to the name of speaker on sessions).
• Has to link to a registration system
• Needs to be under the Kelvar Civic Forum domain www.kelvarcivicforum.example
• Preference to URL kelvarcivicforum.example/Summit2015
Nice to have
• different techniques to display menus, photos and bios and description of sessions
• connect somehow with the visual communication developed on last summit in 2013
Should not have
• should not be the same previously
• should not be traditional
• should not be static

```html
<!DOCTYPE html>
<html lang="en">
<head>
<meta charset="utf-8">
<title>Kelvar Civic Forum Meetup 2015</title>
<link rel="stylesheet" href="https://fonts.googleapis.com/css2?family=Open+Sans:ital,wght@0,300;0,400;0,600;0,700;1,400&display=swap">
<style>
:root{
  --blue:#2f8bd0;
  --blue-dark:#0355a3;
  --link:#1f7fc4;
  --orange:#faa54b;
  --orange-deep:#f37022;
  --green:#9bcb3b;
  --teal:#00a88f;
  --text:#444;
  --muted:#777;
  --rule:#e3e3e3;
  --grey-bg:#f2f2f2;
  --foot-bg:#f7f7f7;
}
*{box-sizing:border-box;margin:0;padding:0}
html,body{width:1200px;height:3508px;overflow:hidden}
body{font-family:"Open Sans",Arial,sans-serif;color:var(--text);background:#fff;position:relative}
.abs{position:absolute}
a{color:var(--link);text-decoration:none}

/* header */
.site-header{position:absolute;left:0;top:0;width:1200px;height:160px;background:#fff}
.world-deco{left:0;top:0;width:330px;height:120px;background:radial-gradient(ellipse at 40% 40%,#e9edf0 0%,#f5f7f8 60%,#fff 100%)}
.brand{left:450px;top:8px;width:300px;text-align:center}
.brand-mark{width:58px;height:58px;border-radius:50%;background:var(--blue-dark);margin:0 auto 6px}
.brand-name{font-size:17px;font-weight:600;color:var(--blue-dark);line-height:1.2}
.partners-top{left:770px;top:16px;display:flex;gap:28px;font-size:12px;font-weight:600;color:var(--teal)}
.partners-top span+span{color:#2a5f3c}
.btn{display:inline-flex;align-items:center;justify-content:center;gap:8px;border-radius:20px;font-weight:600;font-size:13px;text-transform:uppercase;letter-spacing:.3px}
.btn-orange{background:var(--orange);color:#fff}
.register{left:823px;top:68px;width:154px;height:34px}
.main-nav{left:0;top:128px;width:1200px;display:flex;justify-content:center;gap:60px;font-size:14px;color:#555}

/* hero */
.hero{top:160px;height:342px;width:600px}
.hero-left{left:0;background:linear-gradient(160deg,#6f7a6c 0%,#8e9a86 35%,#a9b7a2 60%,#5f6a58 100%)}
.hero-right{left:600px;background:linear-gradient(180deg,#7fb4e2 0%,#b9d6ee 45%,#3e5f8a 70%,#27405f 100%)}
.band{left:0;top:502px;width:1200px;height:162px;background:var(--blue);color:#fff;text-align:center}
.tagline{font-size:17px;font-style:italic;margin-top:20px}
.band h1{font-size:25px;font-weight:400;text-transform:uppercase;margin-top:6px;letter-spacing:.5px}
.band h1 sup{font-size:14px}
.band-meta{display:flex;justify-content:center;align-items:center;gap:22px;margin-top:22px;font-size:15px}
.pill{border:1px solid rgba(255,255,255,.6);border-radius:18px;padding:6px 18px;display:flex;align-items:center;gap:8px}

/* intro */
.col{top:745px;width:372px}
.col h2{font-size:23px;font-weight:400;color:#333;margin-bottom:26px}
.col p{font-size:12.6px;line-height:20px;text-align:justify;margin-bottom:16px;color:#555}
.col-left{left:200px}
.col-right{left:628px}
.building{width:372px;height:142px;background:linear-gradient(180deg,#c9dced 0%,#a45b45 45%,#8a4a3a 70%,#6f8a55 100%);margin-bottom:18px}
.more{font-size:16px;letter-spacing:2px;color:#555;text-align:right;width:372px}
.col-divider{left:600px;top:760px;width:1px;height:480px;background:var(--rule)}

/* speakers */
.section-title{left:0;width:1200px;text-align:center;font-size:23px;font-weight:400;color:#333}
.speakers{left:220px;top:1450px;width:760px;display:flex;justify-content:space-between}
.speaker{width:160px;text-align:center;font-size:13.5px;color:#444}
.avatar{width:110px;height:110px;border-radius:50%;margin:0 auto 26px;border:3px solid #eee}
.carousel-arrow{top:1490px}

/* schedule */
.schedule-text{left:230px;top:1744px;width:740px;text-align:center;font-size:12.8px;line-height:20px;color:#555}
.schedule-btn{left:490px;top:1845px;width:220px;height:34px}

/* sponsors */
.sponsors{left:0;top:1925px;width:1200px;height:684px;background:var(--grey-bg)}
.tier-title{position:absolute;left:0;width:1200px;text-align:center;font-size:17px;color:#555}
.tier-rule{position:absolute;left:0;width:1200px;height:1px;background:#dedede}
.logo-row{position:absolute;left:0;width:1200px;display:flex;justify-content:center;align-items:center}
.sponsor-name{font-weight:700;color:#555;display:flex;align-items:center;gap:8px}
.dot{width:14px;height:14px;border-radius:50%;display:inline-block}
.become{left:505px;top:2514px;width:190px;height:32px;border:1px solid #bbb;color:#888;background:#f8f8f8;font-weight:400;font-size:12px}

/* travel */
.map{left:0;top:2617px;width:600px;height:494px;background:linear-gradient(135deg,#b7d3ea 0%,#cfe2d0 35%,#e9ebe2 60%,#f3efe4 100%)}
.travel{left:652px;top:2636px;width:520px;height:475px;overflow:hidden}
.travel h2{font-size:24px;font-weight:400;color:#333;margin-bottom:10px}
.travel .lead{font-size:13.5px;color:#555}
.travel .note{font-size:11.5px;font-style:italic;color:#888;margin-bottom:14px}
.hotel{margin-bottom:16px}
.hotel h3{font-size:14px;font-weight:600;color:var(--link);margin-bottom:3px}
.hotel p{font-size:11px;line-height:17px;color:#666}
.hotel .btn{background:var(--link);color:#fff;font-size:10.5px;text-transform:none;height:22px;padding:0 14px;margin-top:6px}

/* footer */
.site-footer{left:0;top:3111px;width:1200px;height:349px;background:var(--foot-bg);border-top:1px solid var(--rule)}
.footer-col{top:3132px}
.footer-col h4{font-size:16px;font-weight:400;color:#333;margin-bottom:14px}
.footer-col h5{font-size:13px;font-weight:400;color:#333;margin-bottom:4px}
.footer-col p{font-size:11.5px;color:#777;line-height:18px}
.contact-line{display:flex;gap:26px;font-size:11.5px;color:#666;margin:6px 0 20px}
.contact-line span{display:flex;align-items:center;gap:6px}
.quick{display:grid;grid-template-columns:184px 220px;row-gap:8px;font-size:12px;color:#666}
.copyright{left:0;top:3460px;width:1200px;height:48px;background:#ececec;text-align:center;line-height:48px;font-size:11px;color:#777}
</style>
</head>
<body>

<header class="site-header">
  <div class="abs world-deco" role="img" aria-label="Faint dotted world map decoration"></div>
  <div class="abs brand">
    <div class="brand-mark"></div>
    <div class="brand-name">Kelvar Civic Forum</div>
  </div>
  <div class="abs partners-top"><span>TQR</span><span>Ashcombe University</span></div>
  <a class="abs btn btn-orange register" href="#">Register now
    <svg width="12" height="12" viewBox="0 0 12 12"><circle cx="6" cy="6" r="6" fill="#fff"/><path d="M5 3.5 7.5 6 5 8.5" stroke="#faa54b" stroke-width="1.6" fill="none"/></svg>
  </a>
  <nav class="abs main-nav">
    <a style="color:#555">Kelvar Civic Forum</a><a style="color:#555">Knowledge Base</a><a style="color:#555">Sponsors &amp; Partners</a><a style="color:#555">Join Us</a><a style="color:#555">Events</a><a style="color:#555">Contacts</a>
  </nav>
</header>

<div class="abs hero hero-left" role="img" aria-label="Photo of an informal riverside settlement"></div>
<div class="abs hero hero-right" role="img" aria-label="Photo of wind turbines and solar panels under a blue sky"></div>

<section class="abs band">
  <p class="tagline">"Sustainable Entrepreneurship From The Bottom Up"</p>
  <h1>2<sup>nd</sup> International Kelvar Civic Forum Meetup</h1>
  <div class="band-meta">
    <span>July 15, 16 &amp; 17, 2015</span>
    <span class="pill"><svg width="11" height="15" viewBox="0 0 11 15"><path d="M5.5 0A5.5 5.5 0 0 0 0 5.5C0 9.5 5.5 15 5.5 15S11 9.5 11 5.5A5.5 5.5 0 0 0 5.5 0Z" fill="#fff"/><circle cx="5.5" cy="5.5" r="2" fill="#2f8bd0"/></svg>Alderport, Easterlake</span>
  </div>
</section>

<div class="abs col-divider"></div>
<section class="abs col col-left">
  <h2>The Kelvar Network</h2>
  <p>The Base of the Pyramid (Kelvar) is a socio-economic designation for the more than 4 billion people living on less than $8 a day. It is also a business strategy that focuses on products, services and enterprises to serve this demographic in a way that is culturally sensitive, environmentally sustainable and economically profitable.</p>
  <p>There are tremendous benefits to companies who begin focusing on the poor as business partners and innovators, as well as value-demanding consumers. Companies who choose to serve these new markets will join a unique group of bold visionaries that not only embrace a new brand of corporate social responsibility, but will also experience a new mode of growth and profitability.</p>
  <p>As we witness growing inequality and accelerating environmental degradation around the world, commercial attention in the years ahead will inevitably come to focus more on breakthrough and disruptive innovations that directly confront these challenges. The time is now for entrepreneurs and innovative corporations to take the "Green Leap"— the harnessing of technological and business model innovations to create new growth platforms that regenerate the environment and lift the poor—while simultaneously generating financial returns.</p>
  <div class="more">•••</div>
</section>
<section class="abs col col-right">
  <h2>About 2015 Summit</h2>
  <div class="building" role="img" aria-label="Photo of the brick conference hall on campus"></div>
  <p><a href="#">Tessaro Quorum for Renewal</a> (TQR) and Ashcombe University, in collaboration with the Kelvar Civic Forum Labs from around the world, are organizing the second Kelvar Civic Forum Meetup. The event will be held July 16th and 17th, 2015 at Ashcombe University (AU) <a href="#">Halvern Hall</a> in Alderport, Easterlake.</p>
  <p>The 2015 event will build on the 1st Kelvar Civic Forum Meetup: "Pushing the Boundaries of Kelvar" held in 2013 in Valdoro - Brazil (Sponsored by Lumera, Corvane, Packwell, Ostrel, Brightfield and Arvona), which brought together corporate innovators, academics, entrepreneurs, community leaders, students, and Kelvar Lab leaders from more than 16 countries.</p>
  <div class="more">•••</div>
</section>

<h2 class="abs section-title" style="top:1340px">Speakers &amp; Contributors</h2>
<svg class="abs carousel-arrow" style="left:92px" width="14" height="24" viewBox="0 0 14 24"><path d="M11 3 3 12l8 9" stroke="#888" stroke-width="2.5" fill="none"/></svg>
<svg class="abs carousel-arrow" style="left:1094px" width="14" height="24" viewBox="0 0 14 24"><path d="M3 3l8 9-8 9" stroke="#888" stroke-width="2.5" fill="none"/></svg>
<div class="abs speakers">
  <div class="speaker"><div class="avatar" role="img" aria-label="Portrait of Owen Castell" style="background:radial-gradient(circle at 50% 40%,#d9c3b0,#6a6f78)"></div>Owen Castell</div>
  <div class="speaker"><div class="avatar" role="img" aria-label="Portrait of Miles Tarrant" style="background:radial-gradient(circle at 50% 40%,#e0c8b6,#5d6470)"></div>Miles Tarrant</div>
  <div class="speaker"><div class="avatar" role="img" aria-label="Portrait of Paul Renwick" style="background:radial-gradient(circle at 50% 40%,#d8bca8,#3f3f46)"></div>Paul Renwick</div>
  <div class="speaker"><div class="avatar" role="img" aria-label="Portrait of Imara" style="background:radial-gradient(circle at 50% 40%,#e5c6ad,#6b4a3a)"></div>Imara</div>
</div>

<h2 class="abs section-title" style="top:1677px">Summit Schedule</h2>
<p class="abs schedule-text">The 2nd Kelvar Civic Meetup has been designed to first provoke, then discuss, and finally, act. Accordingly, each segment starts with the "plenary provocation" to challenge and stimulate creative thinking, followed by breakout sessions geared toward building networks, action agendas and new initiatives.</p>
<a class="abs btn btn-orange schedule-btn" href="#">View summit schedule
  <svg width="10" height="12" viewBox="0 0 10 12"><path d="M3 2l4 4-4 4" stroke="#fff" stroke-width="2" fill="none"/></svg></a>

<section class="abs sponsors">
  <div class="tier-title" style="top:46px">Diamond Sponsors</div>
  <div class="logo-row" style="top:110px;gap:78px">
    <span class="sponsor-name" style="font-size:15px"><i class="dot" style="background:#e3872d"></i>Lumera</span>
    <span class="sponsor-name" style="font-size:18px"><i class="dot" style="background:#1f5fa8"></i>Fizzlo</span>
    <span class="sponsor-name" style="font-size:18px"><i class="dot" style="background:#d33"></i>Stonara</span>
    <span class="sponsor-name" style="font-size:14px"><i class="dot" style="background:#1a3e8c"></i>Nordhelm</span>
  </div>
  <div class="tier-rule" style="top:200px"></div>
  <div class="tier-title" style="top:232px">Working Sessions Sponsors</div>
  <div class="logo-row" style="top:274px"><span class="sponsor-name" style="font-size:17px">Weaveline</span></div>
  <div class="tier-rule" style="top:328px"></div>
  <div class="tier-title" style="top:354px">Partners and Collaborators</div>
  <div class="logo-row" style="top:420px;gap:56px">
    <span class="sponsor-name" style="font-size:18px;color:#7a3b52">Halberg</span>
    <span class="sponsor-name" style="font-size:15px;color:#3f8f3f"><i class="dot" style="background:#5aa64a"></i>gcsb</span>
    <span class="sponsor-name" style="font-size:17px;color:#2d5f8a">corvella</span>
    <span class="sponsor-name" style="font-size:13px;color:#2d4f7a"><i class="dot" style="background:#d9a520"></i>Tamsford University</span>
    <span class="sponsor-name" style="font-size:12px;color:#444">Wendell Institute</span>
  </div>
  <div class="logo-row" style="top:496px;gap:70px">
    <span style="width:110px;height:32px;background:#dde6f1;display:inline-block"></span>
    <span class="sponsor-name" style="font-size:13px;color:#333"><i class="dot" style="background:#333"></i>Rootstock</span>
    <span style="width:40px;height:40px;border-radius:50%;background:#cfe3c3;display:inline-block"></span>
  </div>
  <a class="btn become" style="position:absolute;top:589px" href="#">Become a sponsor</a>
</section>

<div class="abs map" role="img" aria-label="Map of Alderport showing hotels and the summit venue"></div>
<section class="abs travel">
  <h2>Travel and Lodging</h2>
  <p class="lead">Map of Alderport, Easterlake with reference of Hotels and Summit Venue</p>
  <p class="note">Map must be interactive. Add discount rate for each hotel</p>
  <div class="hotel">
    <h3>Harborview Court Hotel</h3>
    <p>18 Linden Row, Alderport (0.4 miles from summit venue)<br>1-555-013-7720 (Reservations by phone, reference Kelvar conference rate)<br>Cut-off date: June 15, 2015</p>
    <span class="btn">Reservations</span>
  </div>
  <div class="hotel">
    <h3>Maplecrest Hotel</h3>
    <p>902 Orchard Lane, South Alderport (1.5 miles from summit venue)<br>1-555-016-3391<br>Cut-off date: June 14, 2015</p>
    <span class="btn">Reservations</span>
  </div>
  <div class="hotel">
    <h3>Hotel Easterlake</h3>
    <p>44 Linden Row, Alderport (1.2 miles from summit venue)</p>
  </div>
</section>

<footer class="abs site-footer"></footer>
<div class="abs footer-col" style="left:125px;width:470px">
  <h4>Contact Information</h4>
  <h5>Conference Content Questions</h5>
  <p>Please contact Nadia Korwin for any questions regarding the content of the conference.</p>
  <div class="contact-line">
    <span><svg width="11" height="11" viewBox="0 0 11 11"><path d="M2 0h2l1 3-1.5 1a6 6 0 0 0 3.5 3.5L8 6l3 1v2c0 1-1 2-2 2A9 9 0 0 1 0 2C0 1 1 0 2 0Z" fill="#888"/></svg>(555) 014-2287</span>
    <span><svg width="12" height="9" viewBox="0 0 12 9"><rect x=".5" y=".5" width="11" height="8" fill="none" stroke="#888"/><path d="M.5.5 6 5l5.5-4.5" fill="none" stroke="#888"/></svg><a href="#">nadia.korwin@t7qr.example</a></span>
  </div>
  <h5>Registration Questions</h5>
  <p>Please contact Conference and Event Services for any registration questions or changes.</p>
  <div class="contact-line">
    <span><svg width="11" height="11" viewBox="0 0 11 11"><path d="M2 0h2l1 3-1.5 1a6 6 0 0 0 3.5 3.5L8 6l3 1v2c0 1-1 2-2 2A9 9 0 0 1 0 2C0 1 1 0 2 0Z" fill="#888"/></svg>(555) 019-4410</span>
    <span><svg width="12" height="9" viewBox="0 0 12 9"><rect x=".5" y=".5" width="11" height="8" fill="none" stroke="#888"/><path d="M.5.5 6 5l5.5-4.5" fill="none" stroke="#888"/></svg><a href="#">registration@ashcombe.example</a></span>
  </div>
</div>
<div class="abs footer-col" style="left:653px;width:420px">
  <h4>Quick Links</h4>
  <div class="quick">
    <span>Kelvar Civic Forum</span><span>Speakers and Contributors</span>
    <span>About 2015 Summit</span><span>Summit Schedule</span>
    <span>Knowledge Base</span><span>Program Descriptions</span>
    <span>Sponsors &amp; Partners</span><span>How to Sponsor</span>
    <span>Join Us</span><span>Registration</span>
    <span>Events</span><span>Travel and Lodging</span>
    <span>Contacts</span><span>Alderport and Outdoor Guide Center</span>
  </div>
</div>
<div class="abs copyright">Copyright © 2015 Kelvar Civic Forum. All rights reserved</div>

</body>
</html>
```